Title: Iron Lantern Sub: Rivers carry every morning west - Book cover

I need a complete book cover, front, spine, and back.

Religions Book

This book is more about the Title so it should be strong and serious.

Like the color Deep Red and black, blue. Deep purple
Avoid greens, orange, yellows.

Maybe a picture of a strong hand on the Bible. OR someone yelling.

If any pictures are used they must be 100% royalty free with proof or a buyout of image.

I have attached a couple of designs that the client likes. Just as a reference. The exception they DIDN'T like the pictures in the book cover.

Please ask any questions to clarify.

Please see the file I just uploaded called 'Book Cover samples.png" The clients likes the Title: Copper Vale" the best. Please create a design something closer to this. The like how the title jumps off the page with a 2D look.

Again the Title must standout, and any use of images must be a secondary to the design.

I am happy with we the designs that have been submitted so far.

I hope this helps you get closer.

Thank you

First of all I want to thank you for all of your designs. At the beginning the client thought he would like a picture that represented the title. But after looking at all of the designs. He has now decided NOT to have any pictures.

Here is what he wants

1. BOLD Font (San Serif only) no fancy versions for the Title "IRON LANTERN" in uppercase. The title font should have some dimension to it to appear 2D or 3D looks. Shiny look. It needs to looks like it jumping off the page.

2. The subtitle right below the title in San Serif font)

3. Background solid color either black, dark red, or dark blue. The background can be slightly textured or gradation fill, etc.

4. The cover must have a strong and bold statement.

Thank you again.

Please use this photo on the back cover.

Thank you

• A picture that over powers the Title.

```html
<!DOCTYPE html>
<html lang="en">
<head>
<meta charset="utf-8">
<title>Iron Lantern – Book Cover</title>
<link rel="stylesheet" href="https://fonts.googleapis.com/css2?family=Oswald:wght@400;500;700&family=PT+Sans+Narrow:wght@400;700&display=swap">
<style>
  :root {
    --canvas-bg: #ececec;
    --cover-blue: #22388a;
    --cover-violet: #4b2f7e;
    --cover-wine: #5e1226;
    --cover-deep: #2a070d;
    --title-red: #e8323f;
    --title-red-dark: #9e1524;
    --title-violet: #8a4fc9;
    --title-violet-dark: #4d2387;
    --ink-light: #f2f0f5;
    --ink-soft: #d9d3e4;
    --box-dark: rgba(20, 4, 8, 0.55);
  }
  * { box-sizing: border-box; margin: 0; padding: 0; }
  html, body { width: 1200px; height: 800px; overflow: hidden; }
  body {
    background: var(--canvas-bg);
    display: flex; align-items: center; justify-content: center;
  }
  .book-spread {
    display: flex;
    height: 640px;
    box-shadow: 0 18px 40px rgba(0,0,0,0.25);
  }
  .panel {
    position: relative;
    height: 100%;
    background: linear-gradient(180deg, var(--cover-blue) 0%, var(--cover-violet) 45%, var(--cover-wine) 75%, var(--cover-deep) 100%);
    overflow: hidden;
  }
  .back-cover, .front-cover { width: 430px; }
  .spine {
    width: 40px;
    background: linear-gradient(180deg, #1d2f78 0%, #3f2770 45%, #4f0f20 78%, #22060b 100%);
    border-left: 1px solid rgba(0,0,0,0.35);
    border-right: 1px solid rgba(0,0,0,0.35);
    display: flex; flex-direction: column; align-items: center;
    padding: 18px 0;
    gap: 22px;
  }
  .spine-text {
    writing-mode: vertical-rl;
    font-family: "Oswald", sans-serif;
    white-space: nowrap;
  }
  .spine-subtitle { font-size: 12px; color: var(--ink-light); letter-spacing: 0.5px; }
  .spine-title {
    font-size: 30px; font-weight: 700; color: var(--title-red);
    text-shadow: 0 0 6px rgba(255,255,255,0.35);
    letter-spacing: 1px;
  }
  .spine-author { margin-top: auto; font-size: 11px; color: var(--ink-soft); letter-spacing: 1px; }

  /* Back cover */
  .back-author {
    position: absolute; top: 24px; right: 36px;
    font-family: "Oswald", sans-serif; font-size: 14px;
    color: var(--ink-light); letter-spacing: 0.5px;
  }
  .back-title {
    position: absolute; top: 42px; left: 0; right: 0; text-align: center;
    font-family: "Oswald", sans-serif; font-weight: 700; font-size: 48px;
    color: var(--title-red-dark);
    -webkit-text-stroke: 1px #ff5a66;
    text-shadow: 0 0 8px rgba(255,80,100,0.45);
    letter-spacing: 0.5px;
  }
  .divider {
    display: flex; align-items: center; justify-content: center; gap: 8px;
  }
  .divider-line { height: 1px; background: var(--ink-soft); opacity: 0.8; }
  .flourish {
    width: 34px; height: 8px; border-radius: 4px;
    background: radial-gradient(ellipse at center, rgba(255,255,255,0.85), rgba(255,255,255,0.1));
  }
  .back-divider-top { position: absolute; top: 114px; left: 60px; right: 60px; }
  .back-divider-bottom { position: absolute; top: 160px; left: 60px; right: 60px; }
  .back-divider-top .divider-line, .back-divider-bottom .divider-line { flex: 1; }
  .back-subtitle {
    position: absolute; top: 124px; left: 0; right: 0; text-align: center;
    font-family: "Oswald", sans-serif; font-weight: 500; font-size: 20px;
    color: var(--ink-light); letter-spacing: 0.3px;
  }
  .back-blurb {
    position: absolute; top: 192px; left: 36px; right: 36px;
    font-family: "PT Sans Narrow", sans-serif; font-size: 13.5px; line-height: 1.32;
    color: var(--ink-light); text-align: justify; text-align-last: center;
  }
  .back-boxes {
    position: absolute; bottom: 28px; left: 36px; right: 36px;
    display: flex; justify-content: space-between;
  }
  .back-box {
    width: 128px; height: 84px; background: var(--box-dark);
    display: flex; align-items: center; justify-content: center;
    font-family: "Oswald", sans-serif; font-size: 12px; color: var(--ink-soft);
  }

  /* Front cover */
  .cover-illustration {
    position: absolute; top: 20px; left: 30px; right: 30px; height: 330px;
    background: radial-gradient(ellipse 55% 48% at 50% 30%, rgba(255,255,255,0.95) 0%, rgba(220,225,255,0.7) 25%, rgba(170,150,220,0.35) 55%, rgba(120,90,180,0) 80%);
  }
  .front-title {
    position: absolute; top: 318px; left: 0; right: 0; text-align: center;
    font-family: "Oswald", sans-serif; font-weight: 700; line-height: 0.98;
    letter-spacing: 1px;
  }
  .front-title .line { display: block; }
  .front-title .line-one {
    font-size: 104px; color: var(--title-red);
    text-shadow: 0 0 2px #fff, 0 0 10px rgba(255,255,255,0.55), 3px 4px 0 var(--title-red-dark);
  }
  .front-title .line-two {
    font-size: 84px; color: var(--title-violet);
    text-shadow: 0 0 2px #fff, 0 0 10px rgba(255,255,255,0.45), 3px 4px 0 var(--title-violet-dark);
  }
  .front-divider-top { position: absolute; top: 538px; left: 62px; right: 62px; }
  .front-divider-bottom { position: absolute; top: 584px; left: 62px; right: 62px; }
  .front-divider-top .divider-line, .front-divider-bottom .divider-line { flex: 1; }
  .front-subtitle {
    position: absolute; top: 546px; left: 0; right: 0; text-align: center;
    font-family: "Oswald", sans-serif; font-weight: 500; font-size: 21px;
    color: var(--ink-light); letter-spacing: 0.3px;
  }
  .front-author {
    position: absolute; top: 598px; left: 0; right: 0; text-align: center;
    font-family: "Oswald", sans-serif; font-size: 13px;
    color: var(--ink-light); letter-spacing: 0.5px;
  }
</style>
</head>
<body>
  <div class="book-spread">
    <section class="panel back-cover">
      <p class="back-author">DALE MARROW'S</p>
      <h2 class="back-title">IRON LANTERN</h2>
      <div class="divider back-divider-top">
        <span class="divider-line"></span>
        <span class="flourish" role="img" aria-label="Small ornamental flourish"></span>
        <span class="divider-line"></span>
      </div>
      <p class="back-subtitle">RIVERS CARRY EVERY MORNING WEST</p>
      <div class="divider back-divider-bottom">
        <span class="divider-line"></span>
        <span class="flourish" role="img" aria-label="Small ornamental flourish"></span>
        <span class="divider-line"></span>
      </div>
      <p class="back-blurb">Lorem ipsum dolor sit amet, consectetur adipisicing elit, sed do eiusmod tempor incididunt ut labore et dolore magna aliqua. Ut enim ad minim veniam, quis nostrud exercitation. Lorem ipsum dolor sit amet, consectetur adipisicing elit, sed do eiusmod tempor incididunt ut labore et dolore magna aliqua. Ut enim ad minim veniam, quis nostrud exercitation. Lorem ipsum dolor sit amet, consectetur adipisicing elit, sed do eiusmod tempor incididunt ut labore et dolore magna aliqua. Ut enim ad minim veniam, quis nostrud exercitation. Lorem ipsum dolor sit amet, consectetur adipisicing elit, sed do eiusmod tempor incididunt ut labore et dolore magna aliqua. Ut enim ad minim veniam, quis nostrud exercitation. Lorem ipsum dolor sit amet, consectetur adipisicing elit, sed do eiusmod tempor incididunt ut labore et dolore magna aliqua. Ut enim ad minim veniam, quis nostrud exercitation. Lorem ipsum dolor sit amet, consectetur adipisicing elit, sed do eiusmod tempor incididunt ut labore et dolore magna aliqua. Ut enim ad minim veniam, quis nostrud exercitation.</p>
      <div class="back-boxes">
        <div class="back-box">LOGO</div>
        <div class="back-box">ISBN</div>
      </div>
    </section>

    <section class="panel spine">
      <span class="spine-text spine-subtitle">RIVERS CARRY EVERY MORNING WEST</span>
      <span class="spine-text spine-title">IRON LANTERN</span>
      <span class="spine-text spine-author">DALE MARROW</span>
    </section>

    <section class="panel front-cover">
      <div class="cover-illustration" role="img" aria-label="Illustration: open hands raised toward a glowing cross in radiant light, with white doves and clouds"></div>
      <h1 class="front-title">
        <span class="line line-one">IRON</span>
        <span class="line line-two">LANTERN</span>
      </h1>
      <div class="divider front-divider-top">
        <span class="divider-line"></span>
        <span class="flourish" role="img" aria-label="Small ornamental flourish"></span>
        <span class="divider-line"></span>
      </div>
      <p class="front-subtitle">RIVERS CARRY EVERY MORNING WEST</p>
      <div class="divider front-divider-bottom">
        <span class="divider-line"></span>
        <span class="flourish" role="img" aria-label="Small ornamental flourish"></span>
        <span class="divider-line"></span>
      </div>
      <p class="front-author">DALE MARROW</p>
    </section>
  </div>
</body>
</html>
```